Garden Design Flier

I would like a PDF of this half page A4 flier in soft green tones with dark green leaves.

Target Market(s)

Home owners and real estate agents

Font styles to use
Serif
Other font styles liked:
• Papyrus

Colors
acd136
9bcb3c
cadf82
fefdec

Requirements
Must have
• Green tones
Nice to have
• Leaves, vines, lawns
Should not have
• Open to ideas, but classic style

```html
<!DOCTYPE html>
<html lang="en">
<head>
<meta charset="utf-8">
<title>Parterre Gardens – Flier</title>
<link rel="stylesheet" href="https://fonts.googleapis.com/css2?family=Federo&family=Lato:ital,wght@0,300;0,400;1,300&display=swap">
<style>
  :root {
    --paper: #eaebec;
    --ink: #574a40;
    --ink-soft: #5e5249;
    --sage: #4f6b5e;
    --leaf-light: #cadf82;
    --leaf-mid: #9bcb3c;
    --leaf-deep: #4f8a4a;
  }
  * { margin: 0; padding: 0; box-sizing: border-box; }
  html, body { width: 1200px; height: 846px; overflow: hidden; background: var(--paper); }
  .flier {
    position: relative;
    width: 1200px;
    height: 846px;
    background: var(--paper);
    overflow: hidden;
    font-family: "Lato", sans-serif;
    color: var(--ink);
    text-align: center;
  }
  .foliage { position: absolute; inset: 0; width: 1200px; height: 846px; }
  .content { position: absolute; inset: 0; }
  .brand {
    position: absolute; top: 76px; left: 0; width: 100%;
    font-family: "Federo", serif; font-weight: 400;
    font-size: 70px; letter-spacing: 15px; color: var(--ink);
    line-height: 1;
  }
  .owner {
    position: absolute; top: 160px; left: 0; width: 100%;
    font-size: 29px; font-weight: 300; letter-spacing: 1px; color: var(--ink-soft);
  }
  .credential {
    position: absolute; top: 199px; left: 0; width: 100%;
    font-size: 20px; font-style: italic; font-weight: 300; color: var(--ink-soft);
  }
  .services {
    position: absolute; top: 273px; left: 0; width: 100%;
    display: flex; justify-content: center; align-items: center; gap: 12px;
    font-family: "Federo", serif; font-size: 34px; letter-spacing: 7px; color: var(--sage);
    list-style: none;
  }
  .services .sprig {
    display: inline-block; width: 30px; height: 30px; border-radius: 50%;
    background: radial-gradient(circle, var(--leaf-mid), var(--leaf-light));
    opacity: .85;
  }
  .pitch {
    position: absolute; top: 366px; left: 200px; width: 800px;
    font-size: 25px; font-style: italic; font-weight: 300; line-height: 39px;
    color: var(--ink-soft);
  }
  .phone {
    position: absolute; top: 577px; left: 0; width: 100%;
    font-size: 60px; font-weight: 400; letter-spacing: 2px; color: var(--ink);
    line-height: 1;
  }
  .email {
    position: absolute; top: 638px; left: 0; width: 100%;
    font-size: 25px; font-weight: 300; color: var(--ink); line-height: 32px;
  }
  .abn {
    position: absolute; top: 675px; left: 0; width: 100%;
    font-size: 23px; font-weight: 300; color: var(--ink); line-height: 32px;
  }
</style>
</head>
<body>
<main class="flier">
  <svg class="foliage" viewBox="0 0 1200 846" role="img" aria-label="Watercolour tropical leaves and palm fronds framing the lower edge and sides">
    <defs>
      <linearGradient id="leafTone" x1="0" y1="0" x2="0" y2="1">
        <stop offset="0" stop-color="#cadf82" stop-opacity=".55"/>
        <stop offset=".5" stop-color="#8fbf6a" stop-opacity=".8"/>
        <stop offset="1" stop-color="#4f8a4a"/>
      </linearGradient>
    </defs>
    <path d="M0 846 L0 420 C80 410 170 470 220 560 C270 650 330 722 420 738 L780 738 C870 722 930 650 980 560 C1030 470 1120 400 1200 410 L1200 846 Z" fill="url(#leafTone)"/>
  </svg>

  <section class="content">
    <h1 class="brand">PARTERRE GARDENS</h1>
    <p class="owner">by Liam Hartley</p>
    <p class="credential">Certificate III. Horticulture. Green College. NSW</p>

    <ul class="services">
      <li>DESIGN</li><li class="sprig" role="img" aria-label="small leaf sprig"></li>
      <li>INSTALL</li><li class="sprig" role="img" aria-label="small leaf sprig"></li>
      <li>GROW</li><li class="sprig" role="img" aria-label="small leaf sprig"></li>
      <li>TEND</li><li class="sprig" role="img" aria-label="small leaf sprig"></li>
      <li>ENJOY</li>
    </ul>

    <p class="pitch">All your gardening and landscaping needs from<br>design and installation to general maintenance. Bespoke<br>vegetable gardens and potager design created to suite your<br>site and requirements.</p>

    <p class="phone">0400-128455</p>
    <p class="email">liam@parterregardens.com.au</p>
    <p class="abn">ABN: 51902736418</p>
  </section>
</main>
</body>
</html>
```